Business card design needed

i am a small sized carpentry business looking to generate work in decks, pergolas, small renovations including bathroom renovations or overseeing new homes being built.

Carpentry

R K Carpentry
Marcus Ellery
0417382906
Specialize in quality decks, pergolas, small renovations including bathrooms and housing project management.
FREE QUOTES

```html
<!DOCTYPE html>
<html lang="en">
<head>
<meta charset="UTF-8">
<title>R K Carpentry – Business Card</title>
<link rel="stylesheet" href="https://fonts.googleapis.com/css2?family=Almendra:wght@400&family=Caveat:wght@400&family=Orbitron:wght@400&display=swap">
<style>
  :root {
    --wood-light: #c98a44;
    --wood-mid: #a8642a;
    --wood-dark: #7a4418;
    --brand-yellow: #f6e53a;
    --ink-white: #ffffff;
    --band-tint: rgba(255, 236, 200, 0.22);
    --tagline-gold: #8a5a12;
    --tagline-glow: #ffe9a8;
  }
  html, body {
    margin: 0;
    padding: 0;
    width: 1200px;
    height: 694px;
    overflow: hidden;
    background: #ffffff;
  }
  .card {
    position: relative;
    width: 1200px;
    height: 694px;
    overflow: hidden;
  }
  .card__wood {
    position: absolute;
    inset: 0;
    background: linear-gradient(160deg, var(--wood-mid) 0%, var(--wood-light) 40%, var(--wood-mid) 70%, var(--wood-dark) 100%);
  }
  .card__band {
    position: absolute;
    left: 0;
    top: 565px;
    width: 1200px;
    height: 129px;
    background: var(--band-tint);
  }
  .brand {
    position: absolute;
    left: 84px;
    top: 122px;
    margin: 0;
    font-family: "Orbitron", sans-serif;
    font-weight: 400;
    font-size: 40px;
    line-height: 1;
    color: var(--brand-yellow);
    white-space: nowrap;
  }
  .services {
    position: absolute;
    left: 76px;
    top: 276px;
    margin: 0;
    font-family: "Caveat", cursive;
    font-size: 38px;
    line-height: 47px;
    color: var(--ink-white);
  }
  .contact {
    position: absolute;
    left: 620px;
    top: 262px;
    width: 520px;
    transform: rotate(-14deg);
    transform-origin: center;
    font-family: "Orbitron", sans-serif;
    color: var(--ink-white);
    text-align: right;
    white-space: nowrap;
  }
  .contact__name {
    margin: 0;
    font-size: 48px;
    line-height: 1.3;
    letter-spacing: 1px;
  }
  .contact__phone {
    margin: 0;
    font-size: 48px;
    line-height: 1.3;
    letter-spacing: 1px;
  }
  .tagline {
    position: absolute;
    left: 562px;
    top: 584px;
    width: 640px;
    margin: 0;
    text-align: center;
    font-family: "Almendra", serif;
    font-size: 42px;
    color: var(--tagline-gold);
    text-shadow: 0 0 6px var(--tagline-glow), 0 0 14px var(--tagline-glow), 0 0 22px var(--tagline-glow);
    white-space: nowrap;
  }
</style>
</head>
<body>
  <main class="card">
    <div class="card__wood" role="img" aria-label="Warm timber deck boards running diagonally across the card"></div>
    <div class="card__band"></div>

    <h1 class="brand">R K Carpentry</h1>

    <p class="services">
      Specialize in<br>
      Quality Decks,<br>
      Pergolas,<br>
      Small Renovations<br>
      including bathrooms<br>
      and housing project management.
    </p>

    <div class="contact">
      <p class="contact__name">Marcus Ellery</p>
      <p class="contact__phone">0417382906</p>
    </div>

    <p class="tagline">Measure Twice, Cut Once</p>
  </main>
</body>
</html>
```